Young Balance Support Network

We need a poster explaining that some children live with a disability called Vestibular Disorder. Feel free to ask question. We want you to respect our color code, same as our logo.

Here is our website : http://www.ybsnetwork.org/

We need to sensibilise people about this disability for children.

Industry/Entity Type

Charity

Font styles to use
Serif

Requirements
Must have
• 1. our logo (with all our details) + one of the photo of Marek
• 2. design showing a child with a dizziness for exemple
• 3. a title saying : Aidez-nous à changer la vie des enfants vivant avec un problème vestibulaire
• 4.include the text attached (information flyer YBSN)
• Poster size : 24"X 36"
Should not have
• wheel chair

```html
<!DOCTYPE html>
<html lang="fr">
<head>
<meta charset="utf-8">
<title>Young Balance Support Network – Flyer</title>
<link href="https://fonts.googleapis.com/css2?family=Archivo+Black&family=Lato:wght@300;400;700;900&display=swap" rel="stylesheet">
<style>
  :root {
    --orange: #f9ae1a;
    --navy: #0d4a6b;
    --sky: #29b5e8;
    --green: #a5c93a;
    --ink: #4a4a4a;
    --paper: #ffffff;
    --mist: #e4e4e4;
    --backdrop: #d6d6d6;
  }
  * { margin: 0; padding: 0; box-sizing: border-box; }
  html, body { width: 1058px; height: 1200px; overflow: hidden; }
  body { background: var(--backdrop); font-family: "Lato", sans-serif; position: relative; }

  .flyer {
    position: absolute; left: 109px; top: 20px;
    width: 840px; height: 1160px;
    background: var(--paper);
    box-shadow: 0 6px 24px rgba(0,0,0,.25);
    overflow: hidden;
  }
  .flyer-backdrop { position: absolute; inset: 0; }

  .title {
    position: absolute; top: 92px; left: 0; width: 100%;
    text-align: center;
    font-family: "Archivo Black", sans-serif;
    font-size: 54px; line-height: 1.12;
    color: var(--navy); text-transform: uppercase;
  }

  .news { position: absolute; left: 70px; top: 372px; width: 470px; }
  .news-head { font-size: 48px; font-weight: 400; color: var(--sky); line-height: 1.05; }
  .news-amount { font-size: 40px; font-weight: 300; color: var(--sky); line-height: 1.15; margin-bottom: 16px; }
  .news-text { font-size: 15px; color: var(--ink); line-height: 1.35; margin-bottom: 12px; }

  .brand {
    position: absolute; left: 560px; top: 420px; width: 230px;
    display: flex; flex-direction: column; align-items: center; gap: 14px;
  }
  .brand-dot { width: 110px; height: 110px; border-radius: 50%; background: var(--sky); }
  .brand-name { font-size: 60px; font-weight: 400; color: var(--green); letter-spacing: 3px; }

  .tagline {
    position: absolute; top: 705px; left: 0; width: 100%;
    text-align: center; font-size: 29px; font-weight: 700;
    color: var(--ink); line-height: 1.2;
  }

  .photo-band {
    position: absolute; left: 0; top: 800px; width: 100%; height: 200px;
    background: var(--sky); padding: 12px 0;
    display: grid; grid-template-columns: 1fr 1fr 1fr; gap: 10px;
  }
  .photo { height: 100%; }
  .photo-splash { background: linear-gradient(160deg, #b9d7e6, #4f8fb5 55%, #c96a3a); }
  .photo-ears { background: linear-gradient(135deg, #8d9aa6, #c9b29c 55%, #7b8791); }
  .photo-park { background: linear-gradient(170deg, #9cc7e2, #7fa9b9 45%, #b9a07c); }

  .contact {
    position: absolute; left: 70px; top: 1028px;
    font-size: 27px; font-weight: 900; color: var(--ink); line-height: 1.25;
    font-style: normal;
  }

  .social {
    position: absolute; right: 60px; top: 1034px;
    display: flex; gap: 26px;
  }
  .social-item { display: flex; align-items: center; gap: 10px; font-size: 20px; font-weight: 700; color: var(--ink); }
  .social-square { width: 58px; height: 58px; border-radius: 6px; background: #3567a8; }
  .social-square.alt { background: var(--sky); }
</style>
</head>
<body>
  <main class="flyer">
    <svg class="flyer-backdrop" width="840" height="1160" viewBox="0 0 840 1160" aria-hidden="true">
      <defs>
        <linearGradient id="paperShade" x1="0" y1="0" x2="1" y2="1">
          <stop offset="0" stop-color="#ffffff"/>
          <stop offset="0.6" stop-color="#f3f3f3"/>
          <stop offset="1" stop-color="#dedede"/>
        </linearGradient>
      </defs>
      <rect width="840" height="1160" fill="url(#paperShade)"/>
      <path d="M0 0 H840 V300 C600 280 300 290 0 390 Z" fill="#f9ae1a"/>
      <path d="M0 390 C300 290 600 280 840 300 L840 328 C600 306 300 318 0 416 Z" fill="#cfcfcf"/>
      <path d="M0 416 C300 318 600 306 840 328 L840 338 C600 318 300 332 0 428 Z" fill="#ffffff"/>
    </svg>

    <h1 class="title">Young Balance Support<br>Network</h1>

    <section class="news">
      <h2 class="news-head">Great News</h2>
      <p class="news-amount">CHF 3000.- collected</p>
      <p class="news-text">Bastien, Noémie, Clarisse and Lucien ran to support us. They took up the challenge of running 10km / 20km to support our association.</p>
      <p class="news-text">They counted on you to sponsor their race and they targeted to get CHF 3'000.- ! We did it !</p>
      <p class="news-text">This amount will help our association to raise awarness of this disability by publishing flyers and posters in Swiss and European hospitals !</p>
    </section>

    <div class="brand">
      <span class="brand-dot"></span>
      <span class="brand-name">YBSN</span>
    </div>

    <p class="tagline">Aidez-nous à changer la vie des enfants vivant avec<br>un problème vestibulaire</p>

    <div class="photo-band">
      <div class="photo photo-splash" role="img" aria-label="Photo of a child playing in a water splash park"></div>
      <div class="photo photo-ears" role="img" aria-label="Photo of a young boy covering his ears, feeling dizzy"></div>
      <div class="photo photo-park" role="img" aria-label="Photo of a girl and her mother at a sunny water park"></div>
    </div>

    <address class="contact">
      www.ybsnetwork.org<br>
      info@ybsnetwork.org<br>
      CCP: 17-482053-6
    </address>

    <div class="social">
      <div class="social-item"><span class="social-square"></span>Linkup</div>
      <div class="social-item"><span class="social-square alt"></span>Chirper</div>
    </div>
  </main>
</body>
</html>
```